Business card for denture clinic Gumlyssa

We need a new business card with our new logo. We are a denture clinic in New Zealand with our target market being 45+ years old. We would need a space on the back to write our patients next appointment on. We would space for only one appointment rather than a list. We will attach a photo showing an example of this. But of course, we would like to see your twist on this. We want it to be bold and easy to read and a good mixture of professional but modern. We have attached our logo to be used on the card.

Target Market(s)

People aged 45+ needing dentures

Industry/Entity Type

Dental

Contact Information for Business Card

We want our logo on the front and the space to write an appointment on the back. I've attached an example our our old business card showing this. We need to have the technicians details on the front.

Font styles to use
Sans Serif

Colors
0255a3
919191
fbfbfb

Requirements
Must have
• The following details:
• Ravi Pelling BDT, PGDipCDentTech Marlow
• Dental Prosthetist
• Phone numbers: 0800 47 2150
• 09 571 3294
• Email: ravi@gumlyssa.co.nz
• www.gumlyssa.co.nz
• Address: 418 Whiroa Road
• Kauriwhenua East
• Auckland 0610
Nice to have
• We would like our business cards to have more than just two colours as we want them to be more vibrant. We have uploaded an example of a business card we liked that showed this.

```html
<!DOCTYPE html>
<html lang="en">
<head>
<meta charset="utf-8">
<title>Gumlyssa – Business Card</title>
<link rel="stylesheet" href="https://fonts.googleapis.com/css2?family=Lato:ital,wght@0,400;0,700;0,900;1,400&display=swap">
<style>
  :root {
    --brand-blue: #0360a4;
    --ink: #1e1e1e;
    --paper: #fbfbfb;
    --grey: #919191;
    --stage: #ececec;
    --white: #ffffff;
  }
  * { margin: 0; padding: 0; box-sizing: border-box; }
  html, body {
    width: 1200px; height: 586px; overflow: hidden;
    background: var(--stage);
    font-family: "Lato", sans-serif;
  }
  .stage { position: relative; width: 1200px; height: 586px; }

  .card {
    position: absolute; top: 129px;
    width: 502px; height: 300px;
  }

  /* Back: appointment side */
  .card-back { left: 61px; background: var(--brand-blue); color: var(--white); }
  .card-back .brand-mark {
    position: absolute; left: 226px; top: 28px;
    width: 50px; height: 50px; background: var(--white);
  }
  .card-back .brand-name {
    position: absolute; left: 0; right: 0; top: 86px;
    text-align: center; font-weight: 900; font-size: 30px; letter-spacing: 2px;
  }
  .appointment-title {
    position: absolute; left: 0; right: 0; top: 150px;
    text-align: center; font-weight: 700; font-size: 13.5px; letter-spacing: 4px;
  }
  .appointment-title span { border-bottom: 1.5px solid var(--white); padding-bottom: 2px; }
  .field { position: absolute; top: 220px; width: 204px; }
  .field-date { left: 39px; }
  .field-time { left: 266px; }
  .field label { display: block; font-size: 13px; margin-bottom: 6px; }
  .field .write-box { height: 34px; background: var(--white); border-radius: 4px; }

  /* Front: technician side */
  .card-front { left: 619px; background: var(--paper); }
  .card-front .brand-mark {
    position: absolute; left: 102px; top: 120px;
    width: 34px; height: 34px; background: var(--brand-blue);
  }
  .card-front .brand-name {
    position: absolute; left: 0; width: 238px; top: 158px;
    text-align: center; font-weight: 900; font-size: 19px; letter-spacing: 1.5px;
    color: var(--brand-blue);
  }
  .divider {
    position: absolute; left: 233px; top: 58px; width: 2px; height: 200px;
    background: linear-gradient(to bottom, rgba(3,96,164,0), var(--brand-blue) 50%, rgba(3,96,164,0));
  }
  .technician { position: absolute; left: 262px; top: 64px; width: 212px; }
  .technician-name { font-weight: 700; font-size: 15px; color: var(--brand-blue); white-space: nowrap; }
  .technician-name em { font-weight: 400; font-size: 10.5px; color: var(--ink); margin-left: 5px; }
  .technician-role {
    display: flex; align-items: center; gap: 5px; margin-top: 6px;
    font-weight: 700; font-size: 11px; color: var(--ink);
  }
  .technician-role::after { content: ""; flex: 1; height: 1.5px; background: var(--brand-blue); }

  .contact-list { position: absolute; left: 262px; top: 114px; list-style: none; }
  .contact-list li {
    display: flex; align-items: center; gap: 8px;
    height: 24px; font-size: 12px; color: var(--ink);
  }
  .contact-list svg { width: 17px; height: 17px; flex: none; }

  .address {
    position: absolute; left: 265px; top: 216px;
    font-weight: 700; font-size: 12.5px; line-height: 18px; color: var(--brand-blue);
    font-style: normal;
  }
</style>
</head>
<body>
<main class="stage">

  <section class="card card-back" aria-label="Appointment card">
    <div class="brand-mark"></div>
    <div class="brand-name">GUMLYSSA</div>
    <div class="appointment-title"><span>Your Next Appointment</span></div>
    <div class="field field-date"><label>Date:</label><div class="write-box"></div></div>
    <div class="field field-time"><label>Time:</label><div class="write-box"></div></div>
  </section>

  <section class="card card-front" aria-label="Technician card">
    <div class="brand-mark"></div>
    <div class="brand-name">GUMLYSSA</div>
    <div class="divider"></div>

    <div class="technician">
      <div class="technician-name">Ravi Pelling BDT <em>PGDipCDentTech Marlow</em></div>
      <div class="technician-role">Dental Prosthetist</div>
    </div>

    <ul class="contact-list">
      <li>
        <svg viewBox="0 0 20 20" aria-hidden="true"><circle cx="10" cy="10" r="10" fill="#0360a4"/><path d="M5 8.5c0-1.5 2.3-2.5 5-2.5s5 1 5 2.5v1h-2.5V8.3h-5v1.2H5z M6.5 10.5h7l1 4h-9z" fill="#fff"/><circle cx="10" cy="12.3" r="1.1" fill="#0360a4"/></svg>
        0800 47 2150
      </li>
      <li>
        <svg viewBox="0 0 20 20" aria-hidden="true"><circle cx="10" cy="10" r="10" fill="#0360a4"/><path d="M5 8.5c0-1.5 2.3-2.5 5-2.5s5 1 5 2.5v1h-2.5V8.3h-5v1.2H5z M6.5 10.5h7l1 4h-9z" fill="#fff"/><circle cx="10" cy="12.3" r="1.1" fill="#0360a4"/></svg>
        09 571 3294
      </li>
      <li>
        <svg viewBox="0 0 20 20" aria-hidden="true"><circle cx="10" cy="10" r="10" fill="#0360a4"/><rect x="5" y="6.5" width="10" height="7" rx="0.8" fill="#fff"/><path d="M5.3 7l4.7 3.6L14.7 7" fill="none" stroke="#0360a4" stroke-width="1"/></svg>
        ravi@gumlyssa.co.nz
      </li>
      <li>
        <svg viewBox="0 0 20 20" aria-hidden="true"><circle cx="10" cy="10" r="10" fill="#0360a4"/><g fill="none" stroke="#fff" stroke-width="1"><circle cx="10" cy="10" r="5"/><ellipse cx="10" cy="10" rx="2.2" ry="5"/><path d="M5 10h10M5.8 7.5h8.4M5.8 12.5h8.4"/></g></svg>
        www.gumlyssa.co.nz
      </li>
    </ul>

    <address class="address">418 Whiroa Road,<br>Kauriwhenua East Auckland 0610</address>
  </section>

</main>
</body>
</html>
```